Wine label for new boutique South African wine focused on the USA market.

Wine label required for new ethical south African red wine called PLUMB which stands for 'Marlowe, tolland, brightly and you' but is also a play on 'SA' and that it has a story to tell. Gerald Marlowe is the wine maker, Tolland the farm owner, and Brightly an investor.

Concept is a simple old type writer font on a white/off white label. Front label would say 'Plumb No.1, 2010 Shiraz, South Africa' and similarly a second for another wine 'Plumb No.2, 2010 Cab/Merlot Blend. Maybe the round stain of the bottom of a wine bottle in the bottom corner? Would also like for the 'plumb' to double up as the logo and work in the form of a stamp.

The rear label will need to tell a short story and be able to accommodate the usual boilerplate info. The story will go something like, ' Plumb No.1: It's a long story, but in short we love our wine and we think you will too. The cooling see breezes of the Indian Ocean help define this world class Shiraz from the Western Cape. Aged in french oak for 20 months, the bold flavors will compliment all red meats or simply enjoy on its own. Learn more about our story at www.plumbvintners.example.

The cab/merlot will read similar: Plumb No.2: It's a long story, but in short we love our wine and we think you will too. The cooling see breezes of the Indian Ocean help define this world class red blend from the Western Cape. Aged in french oak for 20 months, this wine will compliment all red meats or simply enjoy on its own. Learn more about our story at www.plumbvintners.example.

Reason: Had some great designs already, but as i get to understand how ArtBazaarly works, I'm keen to explore as many ideas as possible. Neil

Thanks for all the great designs everybody!

We will make a tough decision in the next couple of days.

Regards

Neil

Target Market(s)

Middle class with some wine knowledge. Price point around $20 -30

Industry/Entity Type

Boutique

Requirements
Nice to have
• A small nod to the wine coming from south Africa in the design would be nice but nothing to over the top
Should not have
• Simple and clear font with plenty of empty space on the label

```html
<!DOCTYPE html>
<html lang="en">
<head>
<meta charset="utf-8">
<title>Plumb No. 1 — 2010 Shiraz Front Label</title>
<link rel="stylesheet" href="https://fonts.googleapis.com/css2?family=Open+Sans:wght@300;700&display=swap">
<style>
  :root {
    --page-bg: #ffffff;
    --label-cream: #fdfbe3;
    --label-stripe: #f6f1cf;
    --rule-red: #9e1b1f;
    --brand-ink: #3b2a2a;
    --detail-ink: #9a8a6a;
  }
  * { margin: 0; padding: 0; box-sizing: border-box; }
  html, body {
    width: 1200px;
    height: 960px;
    overflow: hidden;
    background: var(--page-bg);
  }
  .canvas {
    position: relative;
    width: 1200px;
    height: 960px;
  }
  .front-label {
    position: absolute;
    left: 244px;
    top: 88px;
    width: 712px;
    height: 784px;
    background-color: var(--label-cream);
    background-image: repeating-linear-gradient(
      90deg,
      var(--label-cream) 0 6px,
      var(--label-stripe) 6px 8px
    );
    font-family: "Open Sans", sans-serif;
    text-align: center;
  }
  .label-rule {
    position: absolute;
    left: 0;
    right: 0;
    height: 8px;
    background: var(--rule-red);
  }
  .label-rule--top { top: 44px; }
  .label-rule--bottom { bottom: 44px; }
  .brand-name {
    position: absolute;
    left: 0;
    right: 0;
    top: 288px;
    font-weight: 700;
    font-size: 84px;
    letter-spacing: -1px;
    line-height: 1;
    color: var(--brand-ink);
  }
  .wine-details {
    position: absolute;
    left: 0;
    right: 0;
    top: 530px;
    font-weight: 300;
    font-size: 46px;
    line-height: 62px;
    color: var(--detail-ink);
  }
  .wine-details span { display: block; }
</style>
</head>
<body>
  <main class="canvas">
    <section class="front-label" aria-label="Plumb No. 1 front label">
      <div class="label-rule label-rule--top"></div>
      <h1 class="brand-name">PLUMB</h1>
      <p class="wine-details">
        <span class="wine-number">plumb no. 1</span>
        <span class="wine-vintage">2010 Shiraz</span>
      </p>
      <div class="label-rule label-rule--bottom"></div>
    </section>
  </main>
</body>
</html>
```